Birchline Heating & Air

I need a business card made for my company. I would like my new logo for Birchline Heating and Air on the front and my Garage Door on the back.
Front to say -Heating & Air Conditioning , Mini Splits and Heat Pumps, Hydronic In-Floor Heat. Locally Owned and Operated! Licensed, Boned and Insured. Free Estimates on new equipment. 715-408-2159
BGD Back Card, change phone# to 651-374-5810. Remove Commercial and residential and fully sticked vans lines.

```html
<!DOCTYPE html>
<html lang="en">
<head>
<meta charset="utf-8">
<title>Birchline Heating &amp; Air — Business Card</title>
<link rel="stylesheet" href="https://fonts.googleapis.com/css2?family=Montserrat:wght@400;500;700;800&display=swap">
<style>
  :root{
    --page:#e6e6e6;
    --card:#f4f4f4;
    --red:#d71f1f;
    --blue:#0f4e87;
    --blue-dark:#0a3d6e;
    --blue-light:#1262a2;
    --white:#ffffff;
  }
  *{box-sizing:border-box;margin:0;padding:0}
  html,body{width:1200px;height:1200px;overflow:hidden}
  body{background:var(--page);font-family:"Montserrat",sans-serif;position:relative}
  .card{
    position:absolute;left:234px;width:731px;height:418px;
    background:var(--card);overflow:hidden;
    box-shadow:0 6px 18px rgba(0,0,0,.18);
  }
  .card--front{top:160px}
  .card--back{top:632px}
  .brand-name{
    position:absolute;left:0;right:0;text-align:center;
    color:var(--blue);font-weight:800;line-height:1.05;letter-spacing:.5px;
  }
  .card--front .brand-name{top:42px;font-size:44px}
  .card--back .brand-name{top:50px;font-size:44px}
  .phone{
    position:absolute;left:0;right:0;top:210px;
    display:flex;justify-content:center;align-items:center;gap:12px;
    color:var(--blue);font-weight:700;font-size:29px;
  }
  .phone-icon{width:26px;height:26px}
  .services{
    position:absolute;top:269px;height:83px;border-radius:16px;
    background:linear-gradient(90deg,var(--blue-dark),var(--blue-light));
    color:var(--white);font-weight:400;font-size:18.5px;
    display:flex;flex-direction:column;justify-content:center;align-items:center;gap:6px;
  }
  .card--front .services{left:60px;width:611px}
  .card--back .services{left:112px;width:505px}
  .initial{color:var(--red)}
  .sep{margin:0 6px}
  .band{position:absolute;left:0;bottom:0;width:731px;height:47px}
  .band-shape{position:absolute;inset:0;width:100%;height:100%}
  .band-text{
    position:absolute;top:0;height:47px;display:flex;align-items:center;justify-content:center;gap:10px;
    color:var(--white);font-weight:700;font-size:17px;white-space:nowrap;
  }
  .band-text--left{left:20px;width:310px}
  .band-text--right{left:360px;width:365px}
  .band-icon{width:16px;height:16px;flex:0 0 16px}
</style>
</head>
<body>

<section class="card card--front">
  <div class="brand-name">Birchline<br>Heating &amp; Air</div>
  <div class="phone">
    <svg class="phone-icon" viewBox="0 0 24 24" aria-hidden="true"><path fill="#d71f1f" d="M6.6 10.8a15.1 15.1 0 0 0 6.6 6.6l2.2-2.2c.3-.3.7-.4 1-.2 1.1.4 2.3.6 3.6.6.6 0 1 .4 1 1V20c0 .6-.4 1-1 1A17 17 0 0 1 3 4c0-.6.4-1 1-1h3.5c.6 0 1 .4 1 1 0 1.3.2 2.5.6 3.6.1.3 0 .7-.2 1z"/><path fill="none" stroke="#d71f1f" stroke-width="1.6" stroke-linecap="round" d="M14 6.5a4 4 0 0 1 3.5 3.5M14 3a7.5 7.5 0 0 1 7 7"/></svg>
    <span>715-408-2159</span>
  </div>
  <div class="services">
    <p><span class="initial">H</span>eating &amp; Air Conditioning<span class="sep">|</span><span class="initial">L</span>ocally Owned and Operated!</p>
    <p><span class="initial">M</span>ini Splits and Heat Pumps<span class="sep">|</span><span class="initial">H</span>ydronic In-Floor Heat</p>
  </div>
  <div class="band">
    <svg class="band-shape" viewBox="0 0 731 47" preserveAspectRatio="none" aria-hidden="true">
      <polygon points="0,0 358,0 335,47 0,47" fill="#d71f1f"/>
      <polygon points="366,0 731,0 731,47 343,47" fill="#0f4e87"/>
    </svg>
    <div class="band-text band-text--left">Licensed, Boned and Insured</div>
    <div class="band-text band-text--right">Free Estimates on new equipment</div>
  </div>
</section>

<section class="card card--back">
  <div class="brand-name">BGD<br>Birchline Garage Door</div>
  <div class="phone">
    <svg class="phone-icon" viewBox="0 0 24 24" aria-hidden="true"><path fill="#d71f1f" d="M6.6 10.8a15.1 15.1 0 0 0 6.6 6.6l2.2-2.2c.3-.3.7-.4 1-.2 1.1.4 2.3.6 3.6.6.6 0 1 .4 1 1V20c0 .6-.4 1-1 1A17 17 0 0 1 3 4c0-.6.4-1 1-1h3.5c.6 0 1 .4 1 1 0 1.3.2 2.5.6 3.6.1.3 0 .7-.2 1z"/><path fill="none" stroke="#d71f1f" stroke-width="1.6" stroke-linecap="round" d="M14 6.5a4 4 0 0 1 3.5 3.5M14 3a7.5 7.5 0 0 1 7 7"/></svg>
    <span>651-374-5810</span>
  </div>
  <div class="services">
    <p><span class="initial">S</span>ame Day &amp; <span class="initial">E</span>mergency Service</p>
    <p><span class="initial">A</span>ll Major Brands<span class="sep">|</span><span class="initial">L</span>ocally Owned and Operated</p>
  </div>
  <div class="band">
    <svg class="band-shape" viewBox="0 0 731 47" preserveAspectRatio="none" aria-hidden="true">
      <polygon points="0,0 358,0 335,47 0,47" fill="#d71f1f"/>
      <polygon points="366,0 731,0 731,47 343,47" fill="#0f4e87"/>
    </svg>
    <div class="band-text band-text--left">
      <svg class="band-icon" viewBox="0 0 16 16" aria-hidden="true"><circle cx="8" cy="8" r="6.5" fill="none" stroke="#fff" stroke-width="1.6"/><ellipse cx="8" cy="8" rx="2.6" ry="6.5" fill="none" stroke="#fff" stroke-width="1.3"/><line x1="1.5" y1="8" x2="14.5" y2="8" stroke="#fff" stroke-width="1.3"/></svg>
      <span>www.birchlinegaragedoor.com</span>
    </div>
    <div class="band-text band-text--right">
      <svg class="band-icon" viewBox="0 0 16 16" aria-hidden="true"><rect x="1" y="3" width="14" height="10" rx="1" fill="#fff"/><polyline points="1.5,3.5 8,9 14.5,3.5" fill="none" stroke="#0f4e87" stroke-width="1.5"/></svg>
      <span>birchlinegaragedoor@mailbox.com</span>
    </div>
  </div>
</section>

</body>
</html>
```